Volbex (Pathways for trade momentum) website

My plan is to offer a marketplace where by businesses (SME and Corporates) are able to post specific requirements, be that debt funding advice or other types of advice (legal/accountant) on the volbex website and advisors can seek to 'pitch' to the client.

clients should be anonymous - maybe a specific client number? (this is reduces the risk of bypass) and have the ability to choose the advisor via the advisors profile.

Advisors could potential use there Peerlane profile to auto complete on Volbex - not sure if this is possible or costs involved, however this would be ideal.

I would think Wordpress would be the best platform for this type of platform, however I would be guided by the experts.

I would need any code written in html 5 to allow for various devices (mobile, tablets, desktop)

Logo design is currently being completed also via Sketch Hive and I'm finalising colours ext now, so could provide advice in due course.

additional requirements (medium to longer term)
longer term I would be looking to add addition aspects to the site including algorithms, specific financial calculations, some of which I would be able to complete myself.

similar websites would be:
https://www.taskmorn.com.au
http://www.fundvale.com.au

Industry/Entity Type

Debt

Coding

Coded - Design and coding required

```html
<!DOCTYPE html>
<html lang="en">
<head>
<meta charset="utf-8">
<title>Volbex — Pathways for trade momentum</title>
<link href="https://fonts.googleapis.com/css2?family=Roboto:wght@300;400;500;700&display=swap" rel="stylesheet">
<style>
:root{
  --red:#e8344e;
  --green:#7cc242;
  --teal:#1fb36b;
  --blue:#1b8cc0;
  --ink:#2a2a2a;
  --muted:#9a9a9a;
  --line:#e2e2e2;
  --card:#f4f1ea;
  --foot:#2c2c2c;
  --foot-deep:#1f1f1f;
  --foot-text:#a8a8a8;
}
*{margin:0;padding:0;box-sizing:border-box}
html,body{width:1200px;height:3035px;overflow:hidden;background:#fff}
body{font-family:'Roboto',sans-serif;color:var(--ink);position:relative}
.abs{position:absolute}

/* hero */
.hero{left:0;top:0;width:1200px;height:660px;background:linear-gradient(100deg,#b9b4ae 0%,#8f8a85 45%,#6a5a52 75%,#4a3d38 100%)}
.nav-bar{left:120px;top:40px;width:960px;height:56px;border-bottom:2px solid rgba(255,255,255,.8)}
.logo{left:0;top:0;font-size:40px;font-weight:400;color:#fff}
.logo-dot{display:inline-block;width:10px;height:10px;border-radius:50%;background:var(--green);margin-right:6px;vertical-align:middle}
.nav{right:0;top:18px;display:flex;gap:30px;font-size:13px;color:#fff;align-items:center}
.nav .active{position:relative}
.nav .active::after{content:"";position:absolute;left:-8px;right:-8px;top:38px;height:4px;background:var(--green)}
.search{width:32px;height:32px;border-radius:50%;background:#fff;margin-left:-6px}
.hero-title{left:0;width:1200px;top:180px;text-align:center;font-weight:300;font-size:56px;line-height:70px;color:#fff}
.hero-title em{font-style:normal;color:var(--red)}
.hero-sub{left:0;width:1200px;top:332px;text-align:center;font-size:17px;color:#eee;font-weight:300}
.card{top:415px;width:290px;height:195px;background:var(--card);text-align:center;padding:30px 28px 0}
.card h3{font-size:17px;font-weight:400;color:#333;margin-bottom:8px}
.card p{font-size:12.5px;line-height:20px;color:#555}
.card a{display:block;margin-top:10px;font-size:12px;font-weight:500;color:var(--blue);text-decoration:none}
.card a.hot{color:#e46a3c}
.card-icon{top:-22px;left:122px;width:46px;height:46px;border-radius:50%;background:var(--red)}

/* how */
.how-title{left:0;width:1200px;top:765px;text-align:center;font-size:30px;font-weight:400}
.how-sub{left:0;width:1200px;top:812px;text-align:center;font-size:17px;line-height:26px;color:var(--muted);font-weight:300}
.step{top:930px;width:240px}
.step-ring{left:0;top:0;width:66px;height:66px;border-radius:50%;border:2px solid #ddd;background:#fff}
.step-ring.on{background:var(--red);border-color:#f7c4cc;border-width:5px}
.step h4{position:absolute;left:74px;top:16px;font-size:14px;font-weight:400}
.step p{position:absolute;left:74px;top:44px;width:150px;font-size:12px;line-height:21px;color:#666}
.timeline{left:132px;top:1066px;width:938px;height:1px;background:#e5e5e5}
.rule{left:128px;width:944px;height:1px;background:var(--line)}
.cta-title{left:128px;top:1176px;font-size:22px;font-weight:500}
.cta-sub{left:128px;top:1216px;font-size:13px;color:#666}
.cta-btn{left:898px;top:1178px;width:172px;height:44px;border:2px solid #333;border-radius:3px;font-size:12px;letter-spacing:3px;font-weight:500;display:flex;align-items:center;justify-content:center}

/* bands */
.band-a{left:0;top:1320px;width:1200px;height:428px;background:linear-gradient(90deg,#6b4a3c 0%,#8a5a48 40%,#7a4a3c 100%)}
.band-a h2{left:620px;top:68px;font-size:46px;font-weight:300;color:#fff}
.band-a p{left:620px;top:150px;width:460px;font-size:15px;line-height:23px;color:#f2e8e2}
.btn-green{left:620px;top:260px;width:145px;height:36px;background:var(--teal);color:#fff;font-size:12px;display:flex;align-items:center;justify-content:center}
.band-b{left:0;top:1748px;width:1200px;height:428px;background:linear-gradient(90deg,#e9ecee 0%,#dde3e6 35%,#8fa9c0 60%,#6e8fb0 100%)}
.band-b h2{left:168px;top:130px;font-size:50px;font-weight:300;color:#222;letter-spacing:-1px}
.band-b p{left:168px;top:220px;width:460px;font-size:17px;line-height:25px;color:#999;font-weight:300}
.btn-blue{left:168px;top:322px;width:148px;height:36px;background:var(--blue);color:#fff;font-size:12px;display:flex;align-items:center;justify-content:center}

/* partners */
.arrow{top:2225px;width:30px;height:30px;border-radius:50%;border:2px solid #ccc;display:flex;align-items:center;justify-content:center}
.arrow.on{border-color:var(--red)}
.partners{left:128px;top:2300px;width:944px;display:flex;justify-content:space-between;align-items:center;height:70px}
.partner{font-size:26px;font-weight:500;color:#555;display:flex;align-items:center;gap:8px}
.partner .sq{width:22px;height:22px;border-radius:50%;background:#555}
.partner.red{color:var(--red)}
.short-rule{left:548px;top:2430px;width:104px;height:2px;background:#e4e4e4}

/* footer */
.footer{left:0;top:2478px;width:1200px;height:482px;background:var(--foot);border-top:6px solid var(--green)}
.col-head{top:50px;font-size:16px;color:#ddd;font-weight:300;padding-bottom:10px;width:292px;border-bottom:1px solid #3d3d3d}
.news{left:128px;width:292px;height:80px;border-bottom:1px solid #3a3a3a}
.news .thumb{position:absolute;left:0;top:0;width:58px;height:46px;background:linear-gradient(135deg,#6fb24a,#3a86c4)}
.news h5{position:absolute;left:68px;top:6px;font-size:13px;font-weight:400;color:#eee}
.news span{position:absolute;left:68px;top:28px;font-size:11px;color:#888}
.tags{left:447px;top:110px;width:300px;display:flex;flex-wrap:wrap;gap:8px}
.tag{font-size:10px;color:#bbb;background:#3a3a3a;padding:7px 10px;letter-spacing:.5px}
.tag.on{background:var(--green);color:#fff}
.links{left:447px;top:302px;font-size:11px;line-height:19px;color:#888;list-style:none}
.links li::before{content:"› ";color:#bbb}
.links li.on{color:#fff}
.contact{left:770px;top:104px;font-size:11.5px;line-height:19px;color:var(--foot-text)}
.field{left:770px;width:300px;height:30px;background:#262626;font-size:11px;color:#777;padding:8px 10px}
.send{left:950px;top:388px;width:120px;height:30px;background:#1c1c1c;color:#ddd;font-size:11px;display:flex;align-items:center;justify-content:center}
.bottom{left:0;top:2960px;width:1200px;height:75px;background:var(--foot-deep)}
.copy{left:128px;top:30px;font-size:12px;color:#bbb}
.socials{left:848px;top:24px;display:flex;gap:12px;align-items:center}
.socials span{width:22px;height:22px;background:#ddd;border-radius:3px}
.socials span.on{background:#3b5998;width:28px;height:28px}
</style>
</head>
<body>

<section class="abs hero" role="img" aria-label="Photo of a man in glasses resting his chin on his hand"></section>
<header class="abs nav-bar">
  <div class="abs logo"><span class="logo-dot"></span>Volbex</div>
  <nav class="abs nav">
    <span class="active">Home</span><span>Features</span><span>Blog</span><span>Work</span><span>Register Your Business</span><span class="search"></span>
  </nav>
</header>
<h1 class="abs hero-title">We will show you<br>the way to <em>Success!</em></h1>
<p class="abs hero-sub">Give us a chance and we will prove our efficiency!</p>

<div class="abs card" style="left:128px"><span class="abs card-icon"></span><h3>Tell us what you need done</h3><p>Innovative design always develops in tandem with innovative technology, and can never be an end in itself. Morlem mustache readymade thunderclouds</p><a>Learn more ›</a></div>
<div class="abs card" style="left:456px"><span class="abs card-icon"></span><h3>Get competitive quotes</h3><p>Innovative design always develops in tandem with innovative technology, and can never be an end in itself. Morlem mustache readymade thunderclouds</p><a class="hot">Learn more ›</a></div>
<div class="abs card" style="left:783px"><span class="abs card-icon"></span><h3>Hire the best business</h3><p>Innovative design always develops in tandem with innovative technology, and can never be an end in itself. Morlem mustache readymade thunderclouds</p><a>Learn more ›</a></div>

<svg class="abs" style="left:572px;top:698px" width="56" height="36" viewBox="0 0 56 36"><path d="M12 32h32a9 9 0 0 0 0-18 14 14 0 0 0-27-3A10 10 0 0 0 12 32z" fill="none" stroke="#e8344e" stroke-width="2"/></svg>
<h2 class="abs how-title">How does Volbex work?</h2>
<p class="abs how-sub">Take a general look at the process that we use<br>when Implement new Project</p>

<div class="abs step" style="left:128px"><span class="abs step-ring"></span><h4>1. Idea</h4><p>Care and accuracy in the design process</p></div>
<div class="abs step" style="left:368px"><span class="abs step-ring"></span><h4>2. Planning</h4><p>Care and accuracy in the design process</p></div>
<div class="abs step" style="left:608px"><span class="abs step-ring on"></span><h4>3. Create</h4><p>Care and accuracy in the design process</p></div>
<div class="abs step" style="left:848px"><span class="abs step-ring"></span><h4>4. Success</h4><p>Care and accuracy in the design process</p></div>
<div class="abs timeline"></div>
<svg class="abs" style="left:126px;top:1050px" width="950" height="30" viewBox="0 0 950 30">
  <circle cx="6" cy="4" r="4" fill="#999"/><line x1="6" y1="4" x2="6" y2="14" stroke="#999"/>
  <path d="M142 13l6 3-6 3zM382 13l6 3-6 3zM622 13l6 3-6 3zM862 13l6 3-6 3z" fill="#888"/>
  <circle cx="936" cy="16" r="6" fill="none" stroke="#888"/><circle cx="936" cy="16" r="3" fill="#888"/>
</svg>

<div class="abs rule" style="top:1146px"></div>
<h3 class="abs cta-title">Get the best tips and guides on home renovation</h3>
<p class="abs cta-sub">Minimal design helps viewers navigate though the design.</p>
<div class="abs cta-btn">GET A FREE QUOTE</div>
<div class="abs rule" style="top:1262px"></div>

<section class="abs band-a">
  <div class="abs" role="img" aria-label="Photo of a smiling woman in front of a brick wall" style="left:0;top:0;width:1200px;height:428px"></div>
  <h2 class="abs">Lorem Ipsum Dolor Sit</h2>
  <p class="abs">Cred vinyl keffiyeh DIY salvia kale, banh mi before they sold out farm-to-table VHS viral locavore cozy sweater. Lomo wolf viral, mustache readymade thunderclouds keffiyeh craft cider marfa ethical. Wolf salvia freegan</p>
  <div class="abs btn-green">Request Quote</div>
</section>

<section class="abs band-b">
  <div class="abs" role="img" aria-label="Photo of a smiling couple looking at a laptop" style="left:0;top:0;width:1200px;height:428px"></div>
  <h2 class="abs">The Best Tips &amp; Guides</h2>
  <p class="abs">Cred vinyl keffiyeh DIY salvia kale, banh mi before they sold out farm-to-table VHS viral locavore cozy sweater.</p>
  <div class="abs btn-blue">Register Your Business</div>
</section>

<div class="abs arrow on" style="left:563px"><svg width="10" height="10" viewBox="0 0 10 10"><path d="M7 1L3 5l4 4" stroke="#e8344e" stroke-width="2" fill="none"/></svg></div>
<div class="abs arrow" style="left:605px"><svg width="10" height="10" viewBox="0 0 10 10"><path d="M3 1l4 4-4 4" stroke="#bbb" stroke-width="2" fill="none"/></svg></div>
<div class="abs partners">
  <span class="partner red">Norvik</span>
  <span class="partner"><span class="sq"></span>Pellow Foods</span>
  <span class="partner">Quillbay</span>
  <span class="partner">Norvik</span>
  <span class="partner"><span class="sq"></span>Vantro</span>
  <span class="partner">Tarnix</span>
</div>
<div class="abs short-rule"></div>

<footer class="abs footer">
  <h4 class="abs col-head" style="left:128px">Latest News</h4>
  <h4 class="abs col-head" style="left:447px">Tags</h4>
  <h4 class="abs col-head" style="left:770px">Contact info</h4>
  <div class="abs news" style="top:108px"><span class="thumb" role="img" aria-label="News thumbnail"></span><h5>Blog Post Title Example</h5><span>8 Comments</span></div>
  <div class="abs news" style="top:188px"><span class="thumb" role="img" aria-label="News thumbnail"></span><h5>Blog Post Title Example</h5><span>8 Comments</span></div>
  <div class="abs news" style="top:268px"><span class="thumb" role="img" aria-label="News thumbnail"></span><h5>Blog Post Title Example</h5><span>8 Comments</span></div>
  <div class="abs news" style="top:348px;border:none"><span class="thumb" role="img" aria-label="News thumbnail"></span><h5>Blog Post Title Example</h5><span>8 Comments</span></div>
  <div class="abs tags">
    <span class="tag">FEATURES</span><span class="tag">INSPIRATION</span><span class="tag">SHOWCASE</span><span class="tag">GRAPHIC DESIGN</span><span class="tag on">ILLUSTRATION</span><span class="tag">DESIGN</span><span class="tag">WEB DESIGN</span><span class="tag">VIDEO</span><span class="tag">ART</span><span class="tag">NEW WORK</span><span class="tag">ANIMATION</span><span class="tag">RETOUCHING</span><span class="tag">DIGITAL PAINTING</span><span class="tag">CG</span><span class="tag">HOWTO</span>
  </div>
  <h4 class="abs" style="left:447px;top:272px;font-size:16px;color:#ddd;font-weight:300">Partner Websites</h4>
  <ul class="abs links">
    <li>Coral Development Services</li><li class="on">New Energy Corporation</li><li>Maple Web Design Agency</li><li>Green Business Association</li><li>Bright Idea Photography</li>
  </ul>
  <div class="abs contact">48 Harlow Lane, Eastbrook 20518<br>+1 555 0142<br>hello@volbex-mail.com</div>
  <div class="abs field" style="top:176px">Your name</div>
  <div class="abs field" style="top:214px">E-mail</div>
  <div class="abs field" style="top:252px;height:116px">Your message</div>
  <div class="abs send">SEND MESSAGE</div>
</footer>
<div class="abs bottom">
  <p class="abs copy">© 2014 Volbex All Rights Reserved.</p>
  <div class="abs socials"><span class="on"></span><span></span><span></span><span></span><span></span><span></span><span></span></div>
</div>

</body>
</html>
```